Quorn Electrical Flyer

I would like to create a flyer that I can distribute to domestic households outlining the benefits of installing LED down lights in comparison to the older halogen down lights which use more power to run, therefore costing the customer more money.
My aim is to portray the fact that by getting me to install these new LED lights im SAVING the customer money.
I would nee an 'eye catching' headline that will hopefully save my flyer from being thrown out. something along the lines of " SAVE UP TOO $500 A YEAR ON YOUR ELECTRICAL BILL "
The flyer will need to be modern and professional with colour but not too "in your face".
Ive attached some ideas and images that could be used, also two tables that compare the running and replacement cost of the two lights which would be beneficial for the flyer.
I have also attached my company logo which should also be put on the flyer. Thank you
Target Market(s)
Domestic housholds
Industry/Entity Type
Electrical
Look and feel

```html
<!DOCTYPE html>
<html lang="en">
<head>
<meta charset="UTF-8">
<title>Quorn Electrical – LED Downlight Savings Flyer</title>
<link href="https://fonts.googleapis.com/css2?family=Lato:wght@400;700;900&family=Oswald:wght@500;600;700&display=swap" rel="stylesheet">
<style>
  :root{
    --blue-deep:#17238a;
    --blue:#2235b5;
    --blue-bright:#3047d0;
    --blue-text:#2a3bb0;
    --ink:#2b2b2b;
    --grey-light:#eef0f3;
    --grey-mid:#c9ccd2;
    --grey-line:#b7bac0;
    --white:#ffffff;
  }
  *{box-sizing:border-box;margin:0;padding:0}
  html,body{width:842px;height:1200px;overflow:hidden;background:#f4f4f4}
  body{font-family:"Lato",Arial,sans-serif;color:var(--ink)}
  .flyer{position:relative;width:842px;height:1200px;overflow:hidden;
    background:linear-gradient(180deg,var(--blue-bright) 0%,var(--blue) 45%,var(--blue-deep) 100%)}

  .top-area{position:absolute;inset:0 0 auto 0;height:400px}
  .top-area svg{position:absolute;inset:0;width:100%;height:100%}

  .kitchen-photo{position:absolute;left:0;top:0;width:540px;height:340px;
    background:linear-gradient(135deg,#d9dcdf 0%,#b9bcc0 35%,#7d8186 70%,#4a4d52 100%)}

  .brand{position:absolute;left:560px;top:50px;width:260px;text-align:center}
  .brand-mark{width:56px;height:56px;border-radius:50%;background:#3a3a3a;margin:0 auto 20px}
  .brand-name{font-family:"Lato",Arial,sans-serif;font-weight:400;font-size:22px;letter-spacing:3px;color:#3a3a3a;text-transform:uppercase;white-space:nowrap}

  .product{position:absolute;border-radius:50%;border:4px solid var(--white);
    box-shadow:0 4px 10px rgba(0,0,0,.35)}
  .product-a{left:410px;top:290px;width:130px;height:130px;background:radial-gradient(circle,#f6f7f8 0%,#cfd2d6 70%,#9ea2a8 100%)}
  .product-b{left:592px;top:262px;width:136px;height:126px;background:radial-gradient(circle,#e9ebed 0%,#b5b9be 65%,#7f848a 100%)}

  .offer{position:absolute;left:0;top:345px;width:322px;height:272px;background:var(--white);
    border-radius:0 14px 14px 0;padding:30px 0 0 26px;box-shadow:0 3px 8px rgba(0,0,0,.25)}
  .offer-lead{font-family:"Oswald",sans-serif;font-weight:500;font-size:40px;color:#3c3c3c;line-height:1}
  .offer-amount{font-family:"Oswald",sans-serif;font-weight:700;font-size:74px;color:var(--blue-text);line-height:1.05;letter-spacing:1px}
  .offer-sub{font-size:18px;color:#333;letter-spacing:.5px;padding-bottom:8px;border-bottom:1px solid var(--grey-line);width:270px;text-transform:uppercase}
  .offer-note{font-size:16px;color:#333;line-height:1.3;margin-top:8px;width:270px}

  .headline{position:absolute;left:330px;top:448px;width:500px;text-align:center;color:var(--white);
    font-family:"Oswald",sans-serif;font-weight:600;font-style:italic;line-height:1.2;white-space:nowrap;text-shadow:0 2px 3px rgba(0,0,0,.3)}
  .headline .line-1{font-size:31px;display:block}
  .headline .line-2{font-size:42px;display:block}

  .benefits{position:absolute;right:36px;top:575px;width:470px;list-style:none;color:var(--white);font-size:23px;line-height:1.4;text-align:right}
  .benefits li::after{content:"";display:inline-block;width:10px;height:10px;border-radius:50%;background:var(--white);margin-left:12px;vertical-align:middle}

  .cost-panel{position:absolute;left:45px;width:752px;background:linear-gradient(180deg,#ffffff 0%,#e4e6ea 100%);
    border-radius:12px;padding:10px 20px 16px;box-shadow:0 3px 8px rgba(0,0,0,.35)}
  .running{top:690px}
  .replacement{top:912px}
  .panel-title{font-size:15px;font-weight:700;color:var(--blue-text);letter-spacing:.3px;margin-bottom:6px;text-transform:uppercase}
  .cost-table{width:100%;border-collapse:collapse;background:var(--white);font-size:14px}
  .cost-table th,.cost-table td{border:1px solid var(--grey-line);padding:3px 6px;text-align:center}
  .cost-table th{font-weight:700;text-transform:uppercase;font-size:14px;background:var(--grey-light)}

  .section-heading{position:absolute;left:0;width:842px;top:868px;text-align:center;color:var(--white);
    font-size:25px;font-weight:700;letter-spacing:.3px}

  .contact-bar{position:absolute;left:0;bottom:0;width:842px;height:100px;background:var(--white);
    display:flex;align-items:center;justify-content:center;font-size:24px;color:#222;letter-spacing:.4px}
</style>
</head>
<body>
<main class="flyer">

  <section class="top-area">
    <div class="kitchen-photo" role="img" aria-label="Photo of a modern kitchen with downlights and glossy white cabinets"></div>
    <svg viewBox="0 0 842 400" preserveAspectRatio="none" aria-hidden="true">
      <defs>
        <linearGradient id="paper" x1="0" y1="0" x2="1" y2="0">
          <stop offset="0" stop-color="#ffffff" stop-opacity="0"/>
          <stop offset="0.55" stop-color="#f3f4f6" stop-opacity="0.9"/>
          <stop offset="0.75" stop-color="#f4f5f7"/>
          <stop offset="1" stop-color="#e6e8eb"/>
        </linearGradient>
      </defs>
      <path d="M0 0 H842 V200 C700 255 560 300 0 318 Z" fill="url(#paper)"/>
      <path d="M842 200 C700 255 560 300 0 318 V330 C560 314 720 280 842 226 Z" fill="#c9ccd2"/>
      <path d="M842 226 C720 280 560 314 0 330 V340 C560 328 730 296 842 250 Z" fill="#ffffff"/>
    </svg>
    <div class="brand">
      <div class="brand-mark"></div>
      <div class="brand-name">Quorn Electrical</div>
    </div>
    <div class="product product-a" role="img" aria-label="White LED downlight fitting"></div>
    <div class="product product-b" role="img" aria-label="Silver LED downlight fitting"></div>
  </section>

  <aside class="offer">
    <p class="offer-lead">SAVE UP TO</p>
    <p class="offer-amount">$500 OFF</p>
    <p class="offer-sub">Your electricity bill</p>
    <p class="offer-note">Based on changing 20 of your halogen down lights to LED.</p>
  </aside>

  <h1 class="headline">
    <span class="line-1">Are you spending too much money</span>
    <span class="line-2">on your electricity bill?</span>
  </h1>

  <ul class="benefits">
    <li>Sick and tired of changing globes?</li>
    <li>Want to save money while adding<br>value to your house?</li>
  </ul>

  <section class="cost-panel running">
    <h2 class="panel-title">Yearly prices based on 6 hours use per day @$0.30 KW/H</h2>
    <table class="cost-table">
      <thead>
        <tr><th>Number of downlights</th><th>Halogen globe(50W)</th><th>LED(10W)</th><th>Savings</th></tr>
      </thead>
      <tbody>
        <tr><td>1</td><td>$32.85 PER YEAR</td><td>$6.57 PER YEAR</td><td>$26.28</td></tr>
        <tr><td>10</td><td>$328.50</td><td>$65.70</td><td>$262.80</td></tr>
        <tr><td>20</td><td>$657</td><td>$131.40</td><td>$525.60</td></tr>
        <tr><td>30</td><td>$985.50</td><td>$197.10</td><td>$788.40</td></tr>
      </tbody>
    </table>
  </section>

  <h2 class="section-heading">YEARLY PRICES BASED ON 6 HRS USE PER DAY @$0.30 KW/H</h2>

  <section class="cost-panel replacement">
    <h2 class="panel-title">Yearly replacement costs based on 6 hours use per day</h2>
    <table class="cost-table">
      <thead>
        <tr><th>Number of downlights</th><th>Halogen (av.1000 hours)</th><th>LED (av.50000 hours)</th></tr>
      </thead>
      <tbody>
        <tr><td>1</td><td>$10</td><td>$0</td></tr>
        <tr><td>10</td><td>$100</td><td>$0</td></tr>
        <tr><td>20</td><td>$200</td><td>$0</td></tr>
        <tr><td>30</td><td>$300</td><td>$0</td></tr>
      </tbody>
    </table>
  </section>

  <footer class="contact-bar">CONTACT DALE FOR AN OBLIGATION FREE QUOTE: 0400 731 592</footer>

</main>
</body>
</html>
```